hostels chain website in Barcelona

We need a web design for a brand of youth hostels located in Barcelona called El Patio Mirasol. We have two hostels with different location. We offer cheap accomodation in shared dorms for young people (avg. 23 years old), but we aim to arrive to cultural tourist more than party people. We offer a local experience by hiring only local staff and by doing some free activities related to Barcelona.
Updates

Hello, In our website it has to appear the number and logo of the official agency that approve the bussiness. It is in our website, it is an orange box with the number 341 and 729. Besides this, we also like to have the wanderlogue box where it is possible to read reviews. Regards Marisol

Target Market(s)

Young people between 18 to 35 years old, that loves travelling and living new experiences.

Industry/Entity Type

Tourist

Other font styles liked:
• Gladifilthefte and Rockwell

Requirements
Must have
• Pictures of the hostel, booking buttom, groups section and activities section.
It must talk about two different locations.
Colors and design has to be related to the decoration of the hostel and the logo.
Nice to have
• It has to show happiness and cleanliness. we like the website http://www.patiolunahost.com/ as a reference.
Should not have
• Boring things

```html
<!DOCTYPE html>
<html lang="en">
<head>
<meta charset="utf-8">
<title>El Patio Mirasol Hostel</title>
<link rel="stylesheet" href="https://fonts.googleapis.com/css2?family=Arvo:ital,wght@0,400;0,700;1,700&display=swap">
<style>
  :root {
    --teal: #17998b;
    --white: #ffffff;
    --brand-blue: #1c5c8e;
    --sun-yellow: #e6b71e;
    --coral-red: #e23b32;
    --sand: #d8c6b2;
    --sky-dark: #4d5a6e;
    --terrace: #6d5a4c;
  }
  * { margin: 0; padding: 0; box-sizing: border-box; }
  html, body { width: 1200px; height: 749px; overflow: hidden; background: var(--white); }
  body { font-family: "Arvo", Georgia, serif; position: relative; }

  .sidebar { position: absolute; left: 0; top: 0; width: 225px; height: 749px; }
  .brand { height: 305px; background: var(--white); position: relative; }
  .brand-name {
    position: absolute; left: 36px; top: 110px; width: 170px;
    color: var(--brand-blue); font-weight: 700; font-size: 24px; line-height: 30px;
  }
  .brand-mark {
    position: absolute; left: 150px; top: 70px; width: 16px; height: 16px;
    background: var(--brand-blue); border-radius: 50%;
  }
  .nav { background: var(--teal); height: 444px; position: relative; color: var(--white); }
  .nav a { color: var(--white); text-decoration: none; display: block; position: absolute; left: 42px; }
  .nav .hostel-link { font-weight: 700; font-size: 14px; letter-spacing: 0.4px; }
  .nav .page-link { font-size: 14px; line-height: 14px; }
  .copyright { position: absolute; left: 42px; top: 427px; font-size: 9px; color: var(--white); }

  .hero { position: absolute; left: 225px; top: 0; width: 975px; height: 749px; }
  .hero-photo {
    position: absolute; inset: 0;
    background:
      linear-gradient(90deg, rgba(92,74,58,0.55) 0%, rgba(92,74,58,0.15) 40%, rgba(70,84,60,0.1) 75%, rgba(60,70,50,0.45) 100%),
      linear-gradient(180deg, #4f5b70 0%, #6f7480 18%, #8a8580 32%, #6c5d50 48%, #5f5a48 66%, #6b5747 84%, #5c4a3d 100%);
  }
  .hero-art { position: absolute; left: 0; top: 0; }
  .card-title { font-family: "Arvo", Georgia, serif; font-weight: 700; font-size: 33px; fill: var(--white); }
  .card-sub { font-family: "Arvo", Georgia, serif; font-weight: 700; font-style: italic; font-size: 16px; fill: var(--white); }
  .book-label { font-family: "Arvo", Georgia, serif; font-weight: 700; font-style: italic; font-size: 16px; fill: var(--white); }

  .languages { position: absolute; right: 25px; top: 18px; display: flex; gap: 9px; }
  .languages svg { display: block; }
</style>
</head>
<body>
  <aside class="sidebar">
    <div class="brand">
      <span class="brand-mark"></span>
      <div class="brand-name">El Patio<br>Mirasol<br>hostel</div>
    </div>
    <nav class="nav">
      <a class="hostel-link" href="#" style="top:38px">LA PEDRERA</a>
      <a class="hostel-link" href="#" style="top:70px">PARK GUELL</a>
      <a class="page-link" href="#" style="top:141px">Bookings<br>&amp; Prices</a>
      <a class="page-link" href="#" style="top:183px">Location</a>
      <a class="page-link" href="#" style="top:211px">Gallery</a>
      <a class="page-link" href="#" style="top:239px">Activities</a>
      <a class="page-link" href="#" style="top:267px">Groups</a>
      <a class="page-link" href="#" style="top:295px">Attractions<br>in Barcelona</a>
      <a class="page-link" href="#" style="top:337px">Reviews</a>
      <a class="page-link" href="#" style="top:365px">Contact us</a>
      <p class="copyright">Copyright @ 2014</p>
    </nav>
  </aside>

  <main class="hero">
    <div class="hero-photo" role="img" aria-label="Hostel roof terrace with wooden fence, potted palms and folding chairs under a cloudy sky"></div>

    <svg class="hero-art" width="975" height="749" viewBox="225 0 975 749">
      <defs>
        <linearGradient id="pedrera-room" x1="0" y1="0" x2="0" y2="1">
          <stop offset="0" stop-color="#e9bb22"/>
          <stop offset="0.62" stop-color="#e2b21f"/>
          <stop offset="0.78" stop-color="#c9a43a"/>
          <stop offset="0.88" stop-color="#ecebe8"/>
          <stop offset="1" stop-color="#dcdad6"/>
        </linearGradient>
        <linearGradient id="guell-room" x1="0" y1="0" x2="0" y2="1">
          <stop offset="0" stop-color="#a87a52"/>
          <stop offset="0.3" stop-color="#c99b6f"/>
          <stop offset="0.55" stop-color="#d9c5b0"/>
          <stop offset="0.8" stop-color="#efe9e2"/>
          <stop offset="1" stop-color="#f6f3ef"/>
        </linearGradient>
      </defs>
      <g class="location-card">
        <polygon points="350,330 485,275 620,290 672,378 660,490 490,520 445,495" fill="url(#pedrera-room)" role="img" aria-label="Bright dorm room at the La Pedrera hostel with yellow walls and bunk bed"/>
        <text class="card-title" x="395" y="408" textLength="232" lengthAdjust="spacingAndGlyphs">LA PEDRERA</text>
        <text class="card-sub" x="395" y="427">Location</text>
        <polygon points="405,494 528,519 520,535 372,553" fill="var(--sun-yellow)"/>
        <polygon points="512,522 552,512 558,548" fill="var(--sun-yellow)"/>
        <text class="book-label" x="388" y="539" textLength="109" lengthAdjust="spacingAndGlyphs">BOOK NOW!</text>
      </g>
      <g class="location-card">
        <polygon points="735,345 795,270 962,275 1025,322 1058,416 935,503 790,490 760,440" fill="url(#guell-room)" role="img" aria-label="Clean dorm room at the Park Guell hostel with wood panelling and white bed"/>
        <text class="card-title" x="778" y="408" textLength="232" lengthAdjust="spacingAndGlyphs">PARK GUELL</text>
        <text class="card-sub" x="778" y="427">Location</text>
        <polygon points="785,520 900,504 918,528 870,575 778,553" fill="var(--coral-red)"/>
        <polygon points="920,528 955,510 948,548" fill="var(--coral-red)"/>
        <text class="book-label" x="793" y="543" textLength="110" lengthAdjust="spacingAndGlyphs">BOOK NOW!</text>
      </g>
    </svg>

    <div class="languages" aria-label="Language">
      <svg width="20" height="13" viewBox="0 0 20 13" aria-label="English"><rect width="20" height="13" fill="#2a3f8f"/><path d="M0 0L20 13M20 0L0 13" stroke="#fff" stroke-width="2.5"/><path d="M10 0V13M0 6.5H20" stroke="#fff" stroke-width="4"/><path d="M10 0V13M0 6.5H20" stroke="#d22" stroke-width="2"/></svg>
      <svg width="20" height="13" viewBox="0 0 20 13" aria-label="Español"><rect width="20" height="13" fill="#c8202b"/><rect y="3.25" width="20" height="6.5" fill="#f4c20d"/></svg>
      <svg width="20" height="13" viewBox="0 0 20 13" aria-label="Català"><rect width="20" height="13" fill="#f4c20d"/><g fill="#d22"><rect y="1.4" width="20" height="1.45"/><rect y="4.3" width="20" height="1.45"/><rect y="7.2" width="20" height="1.45"/><rect y="10.1" width="20" height="1.45"/></g></svg>
    </div>
  </main>
</body>
</html>
```